ご提案有難うございました。
最もサイトのトンマナにあっており、かつキャンペーンの売りが目立っていると感じたため、こちらのデザインを採用させて頂きました。
どれも素晴らしいご提案で御座いました。
また機会があればどうぞ宜しくお願い致します。
居酒屋予約 バナーデザイン バナー作成の仕事の依頼
希望する色 特になし・その他
バナーサイズ
• 300x250
目的・概要
居酒屋の割引キャンペーンページに誘導するために使用するバナー制作です。
依頼詳細
以下のページ等に設置致します。
https://www.quorvelia.com/asia/japan/japa-japan/japa-restaurant/shinjuku-izakaya/
▽入れてほしい画像▽
会社ロゴ
▽入れてほしい文言▽
※以下の文章例を参考に、バナーデザインに映えるようご調整ください
■文章例
【最大100%割引】税込み2,160円以上の飲食で2,000円のキャッシュバックキャンペーン中!
【最大100%割引】居酒屋利用で2,000円のキャッシュバックキャンペーン中!
【最大100%割引】2,160円(税込)以上の居酒屋利用で2,000円の現金還元中!
Quorvelia限定!居酒屋の利用で現金2,000円が貰える!
【最大100%割引】税込み2,160円の居酒屋利用で2,000円現金還元中!
Quorvelia限定企画!税込み2,160円の居酒屋利用で2,000円現金還元中!!
3000店舗以上から選べる!税込み2,160円の居酒屋利用で2,000円現金還元中!!
居酒屋代金、実質最大100%オフ
3000店以上の居酒屋が実質最大100%割引
居酒屋の利用で漏れなく現金2,000円が貰える
▽バナーサイズ▽
▽納品形式▽
png/jpg
▽注意点・禁止事項▽
※他のクライアントへ既に提案した内容の転用など
※作成いただいたバナーに関して、納品後はクライアントに帰属します。
たくさんのウェブデザイナーの方からのご提案をお待ちしております!

```html
<!DOCTYPE html>
<html lang="ja">
<head>
<meta charset="utf-8">
<title>居酒屋キャンペーン バナー</title>
<link href="https://fonts.googleapis.com/css2?family=Noto+Sans+JP:wght@700;900&display=swap" rel="stylesheet">
<style>
  :root {
    --page-bg: #ffffff;
    --footer-bg: #ffffff;
    --brand-blue: #1a6fc4;
    --button-top: #3f9ae8;
    --button-bottom: #145fb8;
    --badge-red: #e8401c;
    --badge-red-dark: #b92a0c;
    --gold-light: #fff27a;
    --gold-mid: #ffd21e;
    --gold-deep: #f0a400;
    --cash-red: #e4151b;
    --ink-dark: #2a1a08;
    --white: #ffffff;
    --photo-dark-1: #2a2622;
    --photo-dark-2: #5a4a34;
    --photo-dark-3: #8a6a3a;
    --photo-gold-1: #f6c400;
    --photo-gold-2: #ffe56a;
    --photo-gold-3: #d98c00;
    --frame: #cfcfcf;
  }
  * { margin: 0; padding: 0; box-sizing: border-box; }
  html, body {
    width: 1200px; height: 708px; overflow: hidden;
    background: var(--page-bg);
    font-family: "Noto Sans JP", sans-serif;
  }
  .showcase { position: relative; width: 1200px; height: 708px; }
  .banner {
    position: absolute; top: 176px;
    width: 472px; height: 374px;
    overflow: hidden;
    border: 1px solid var(--frame);
  }
  .banner--night { left: 106px; }
  .banner--gold { left: 636px; }

  .banner__photo { position: absolute; inset: 0 0 76px 0; }
  .banner--night .banner__photo {
    background:
      radial-gradient(ellipse 60% 70% at 18% 55%, var(--photo-dark-3) 0%, transparent 70%),
      radial-gradient(ellipse 50% 60% at 85% 80%, var(--photo-dark-2) 0%, transparent 70%),
      linear-gradient(160deg, var(--photo-dark-2), var(--photo-dark-1) 60%);
  }
  .banner--gold .banner__photo {
    background:
      radial-gradient(ellipse 45% 60% at 20% 40%, var(--photo-gold-2) 0%, transparent 70%),
      radial-gradient(ellipse 50% 60% at 80% 70%, var(--photo-gold-2) 0%, transparent 70%),
      linear-gradient(170deg, var(--photo-gold-1), var(--photo-gold-3));
  }

  .banner__copy { position: absolute; left: 22px; top: 14px; line-height: 1; font-weight: 900; }
  .copy__price-note { font-size: 25px; letter-spacing: -0.5px; }
  .copy__usage { font-size: 44px; margin-top: 8px; letter-spacing: -1px; }
  .copy__amount { font-size: 72px; margin-top: 8px; letter-spacing: -2px; }
  .copy__amount small { font-size: 54px; }
  .copy__cashback { font-size: 62px; margin-top: 8px; letter-spacing: -2px; }

  .banner--night .copy__price-note,
  .banner--night .copy__usage { color: var(--white); }
  .banner--night .copy__amount,
  .banner--night .copy__cashback {
    background: linear-gradient(180deg, var(--gold-light), var(--gold-mid) 55%, var(--gold-deep));
    -webkit-background-clip: text; background-clip: text; color: transparent;
  }
  .banner--gold .copy__price-note,
  .banner--gold .copy__usage {
    color: var(--ink-dark);
    -webkit-text-stroke: 6px var(--white); paint-order: stroke fill;
  }
  .banner--gold .copy__amount,
  .banner--gold .copy__cashback {
    color: var(--cash-red);
    -webkit-text-stroke: 6px var(--white); paint-order: stroke fill;
  }

  .banner__badge {
    position: absolute; left: 316px; top: 0;
    width: 128px; height: 128px; border-radius: 50%;
    background: radial-gradient(circle at 40% 35%, var(--badge-red), var(--badge-red-dark));
    border: 3px solid var(--white);
    color: var(--white); font-weight: 900; text-align: center;
    display: flex; flex-direction: column; justify-content: center; line-height: 1.02;
    transform: rotate(8deg);
  }
  .badge__top { font-size: 26px; }
  .badge__pct { font-size: 30px; letter-spacing: -1px; }
  .badge__bottom { font-size: 26px; }

  .banner__footer {
    position: absolute; left: 0; right: 0; bottom: 0; height: 76px;
    background: var(--footer-bg);
    display: flex; align-items: center; justify-content: space-between;
    padding: 0 30px 0 18px;
  }
  .brand { display: flex; align-items: center; gap: 6px; color: var(--brand-blue); font-weight: 900; font-size: 24px; }
  .brand__dot { width: 14px; height: 14px; border-radius: 50%; background: var(--brand-blue); }
  .cta {
    width: 236px; height: 52px; border-radius: 6px;
    background: linear-gradient(180deg, var(--button-top), var(--button-bottom));
    color: var(--white); font-weight: 700; font-size: 24px;
    display: flex; align-items: center; justify-content: center; gap: 10px;
  }
  .cta svg { width: 14px; height: 16px; }
</style>
</head>
<body>
<main class="showcase">
  <section class="banner banner--night">
    <div class="banner__photo" role="img" aria-label="居酒屋の生ビールと料理の写真、暗めのトーン"></div>
    <div class="banner__copy">
      <p class="copy__price-note">税込み2160円の</p>
      <p class="copy__usage">居酒屋利用で</p>
      <p class="copy__amount">2000<small>円</small></p>
      <p class="copy__cashback">現金還元中!!</p>
    </div>
    <div class="banner__badge"><span class="badge__top">最大</span><span class="badge__pct">100%</span><span class="badge__bottom">割引</span></div>
    <div class="banner__footer">
      <span class="brand"><span class="brand__dot"></span>Quorvelia</span>
      <span class="cta">詳しくはこちら<svg viewBox="0 0 14 16"><path d="M0 0 L14 8 L0 16 Z" fill="#fff"/></svg></span>
    </div>
  </section>

  <section class="banner banner--gold">
    <div class="banner__photo" role="img" aria-label="黄金色に輝く生ビールの写真"></div>
    <div class="banner__copy">
      <p class="copy__price-note">税込み2160円の</p>
      <p class="copy__usage">居酒屋利用で</p>
      <p class="copy__amount">2000<small>円</small></p>
      <p class="copy__cashback">現金還元中!!</p>
    </div>
    <div class="banner__badge"><span class="badge__top">最大</span><span class="badge__pct">100%</span><span class="badge__bottom">割引</span></div>
    <div class="banner__footer">
      <span class="brand"><span class="brand__dot"></span>Quorvelia</span>
      <span class="cta">詳しくはこちら<svg viewBox="0 0 14 16"><path d="M0 0 L14 8 L0 16 Z" fill="#fff"/></svg></span>
    </div>
  </section>
</main>
</body>
</html>
```